New Packaging Design Project

Wine packaging redesign. Retail partner requested a redesign of a private label wine. The old label is attached. Our partner liked the Lantern and Briar label and wanted something similar. There will be a logo added to the top of the label

Went on vacation/holiday

```html
<!DOCTYPE html>
<html lang="en">
<head>
<meta charset="utf-8">
<title>Red Blend Wine Label</title>
<link rel="stylesheet" href="https://fonts.googleapis.com/css2?family=Libre+Caslon+Text:wght@400;700&display=swap">
<style>
  :root {
    --backdrop: #1c1a19;
    --label: #4f4b49;
    --label-edge: #5a5553;
    --gold: #d9bf93;
    --silver: #b9b3ae;
    --muted: #a39d98;
    --ornament-warm: #6e6253;
    --ornament-cool: #575250;
  }
  * { margin: 0; padding: 0; box-sizing: border-box; }
  html, body {
    width: 1199px;
    height: 1200px;
    overflow: hidden;
    background: var(--backdrop);
  }
  .canvas {
    position: relative;
    width: 1199px;
    height: 1200px;
  }
  .label {
    position: absolute;
    left: 184px;
    top: 105px;
    width: 830px;
    height: 990px;
    background: linear-gradient(90deg, var(--label) 0%, var(--label-edge) 50%, var(--label) 100%);
    font-family: "Libre Caslon Text", Georgia, serif;
    text-align: center;
  }
  .label__region {
    position: absolute;
    left: 0;
    right: 0;
    top: 48px;
    font-size: 82px;
    font-weight: 400;
    letter-spacing: 3px;
    color: var(--gold);
  }
  .label__style {
    position: absolute;
    left: 0;
    right: 0;
    top: 150px;
    font-size: 44px;
    font-weight: 700;
    letter-spacing: 1px;
    color: var(--silver);
  }
  .label__artwork {
    position: absolute;
    left: 165px;
    top: 270px;
    width: 500px;
    height: 380px;
    background: linear-gradient(135deg, var(--ornament-warm) 0%, var(--ornament-cool) 100%);
  }
  .label__grapes {
    position: absolute;
    left: 0;
    right: 0;
    top: 800px;
    font-size: 23px;
    line-height: 40px;
    letter-spacing: 1px;
    color: var(--muted);
  }
  .label__vintage {
    position: absolute;
    left: 0;
    right: 0;
    top: 902px;
    font-size: 44px;
    color: var(--silver);
  }
</style>
</head>
<body>
  <main class="canvas">
    <section class="label">
      <h1 class="label__region">NAPA VALLEY</h1>
      <h2 class="label__style">RED BLEND</h2>
      <div class="label__artwork" role="img" aria-label="Gold foil line-art emblem"></div>
      <p class="label__grapes">MERLOT | CABERNET SAUVIGNON<br>CABERNET FRANC | PETIT VERDOT | MALBEC</p>
      <p class="label__vintage">2020</p>
    </section>
  </main>
</body>
</html>
```